Unique & Creative Business Card for Lumivaleta

Would you please create a unique design that is soft and appealing to people who seek to raise vibrational energy for themselves, for animals (domestic or wild), or for the environment.

Optional: Elements could include, landscapes, wild animals, feathers, vibrational patterns, the elements (Earth, water, fire, air and space). Images that are calming.

With Thanks!

Target Market(s)

People and businesses who are into the environment, animal welfare, alternative health.

Contact Information for Business Card

Moira Tess
Energist
mt@lumivaleta.example
lumivaleta.example

Requirements
Must have
• Lumivaleta logo (attached)
Symbols that represent our main services: Natural environment, animal, human and energy.
Our strapline ‘Cultivating Resonant Stillness’
Nice to have
• Clear and easy to read
Colours based on nature/soft colours

```html
<!DOCTYPE html>
<html lang="en">
<head>
<meta charset="utf-8">
<title>Lumivaleta – Business Card</title>
<link href="https://fonts.googleapis.com/css2?family=Arimo:wght@400;700&display=swap" rel="stylesheet">
<style>
  :root {
    --backdrop: #151515;
    --card: #ffffff;
    --edge: #2d4f9c;
    --navy: #2b4a8f;
    --sky: #5b87c5;
    --lavender: #e6dcec;
    --divider: #e3d8ea;
  }
  * { box-sizing: border-box; margin: 0; padding: 0; }
  html, body {
    width: 1200px; height: 820px; overflow: hidden;
    background: var(--backdrop);
    font-family: "Arimo", Arial, sans-serif;
  }
  .stage {
    position: relative; width: 1200px; height: 820px;
    display: flex; align-items: center; justify-content: center; gap: 50px;
  }
  .card {
    position: relative; width: 540px; height: 310px;
    background: var(--card);
    border-bottom: 4px solid var(--edge);
    border-right: 2px solid var(--edge);
    overflow: hidden;
  }
  /* front */
  .card-front { display: flex; align-items: center; }
  .brand {
    width: 270px; display: flex; align-items: center; justify-content: center; gap: 12px;
  }
  .brand-dot {
    width: 26px; height: 26px; border-radius: 50%; background: var(--lavender); flex: none;
  }
  .brand-name {
    font-size: 24px; font-weight: 400; letter-spacing: 1px;
    color: var(--navy); text-transform: uppercase; white-space: nowrap;
  }
  .divider {
    width: 1px; height: 160px; background: var(--divider); flex: none;
  }
  .contact { padding-left: 24px; }
  .person-name {
    font-size: 22px; font-weight: 700; color: var(--navy);
    text-transform: uppercase; letter-spacing: 0.5px; white-space: nowrap;
  }
  .person-role { font-size: 15px; color: var(--sky); margin-top: 2px; }
  .details { list-style: none; margin-top: 18px; }
  .details li {
    display: flex; align-items: center; gap: 8px;
    font-size: 14px; color: var(--sky); line-height: 22px; white-space: nowrap;
  }
  .details svg { width: 13px; height: 13px; flex: none; }
  /* back */
  .card-back {
    display: flex; flex-direction: column; align-items: center; justify-content: center; gap: 14px;
  }
  .card-back .brand { width: auto; }
  .strapline {
    font-size: 15px; color: var(--navy); text-transform: uppercase; letter-spacing: 1px; white-space: nowrap;
  }
</style>
</head>
<body>
<main class="stage">
  <section class="card card-front">
    <div class="brand">
      <span class="brand-dot"></span>
      <span class="brand-name">Lumivaleta</span>
    </div>
    <div class="divider"></div>
    <div class="contact">
      <h1 class="person-name">Moira Tess</h1>
      <p class="person-role">Energist</p>
      <ul class="details">
        <li>
          <svg viewBox="0 0 16 16" aria-hidden="true"><path fill="#2b4a8f" d="M3.6 1.2l2.4 2.6-1.3 1.9c.9 2 2.5 3.6 4.6 4.6l1.9-1.3 2.6 2.4-1.4 2.6C6.6 13.8 2.2 9.4 1 3z"/></svg>
          5550142286
        </li>
        <li>
          <svg viewBox="0 0 16 16" aria-hidden="true"><rect x="1" y="3" width="14" height="10" fill="#2b4a8f"/><path d="M1 3l7 6 7-6" fill="none" stroke="#fff" stroke-width="1.2"/></svg>
          mt@lumivaleta.example
        </li>
        <li>
          <svg viewBox="0 0 16 16" aria-hidden="true"><circle cx="8" cy="8" r="7" fill="#2b4a8f"/><g fill="none" stroke="#fff" stroke-width="0.9"><ellipse cx="8" cy="8" rx="3" ry="7"/><path d="M1 8h14M2.5 4.5h11M2.5 11.5h11"/></g></svg>
          www.lumivaleta.example
        </li>
      </ul>
    </div>
  </section>

  <section class="card card-back">
    <div class="brand">
      <span class="brand-dot"></span>
      <span class="brand-name">Lumivaleta</span>
    </div>
    <p class="strapline">Cultivating Resonant Stillness</p>
  </section>
</main>
</body>
</html>
```